【デザイン】

上記のが概要となり、その他は本ページ及び添付資料をご参照頂ますよう御願致します。
※添付資料にはサイト構造など、リニューアル後のサイトマップの情報が含まれますが、あくまでも本件はデザインのみのご依頼です。

サイトの方向性としましては、ITやAI、テクノロジーを連想させるような、可能であればTOPは少し動きがあるとよいのです。また現在はかなり堅苦しい「コーポレートサイト」となっていますが、以前は隠しページや、写真の紹介など、少し笑えるコンテンツを載せていたこともあり、ご提案としましては、少し奇抜なアイディアを歓迎致します。

ご提案いただきたいページとしましてはPC/SPそれぞれの
・TOPページ
・サブページ
のイメージ、合計4点となります。
最初はTOPページ2点のみでも検討させていただきます。

【その他】
最初にTOPデザイン(PC/SP)のご提案をコンペ形式頂きまして、確定させていただきました方に、コーディングを含めてお願いしたいと考えております。

※ご提案の際には、コーディングも可能かどうかと、おおよそのコーディング代の目安も添えていただけますと幸いです。

どうぞ宜しくお願い申し上げます。
www.hinata-reku.co.jp
4ページ
シンプル 複雑
単色 カラフル
暗い 明るい
日常 高級
遊び心 厳粛
未来的 伝統的
女性的 男性的
赤系、グレー系、現在の配色をご参考にお願い致します。
• イラストレーター形式 (.ai)
• フォトショップ形式 (.psd)
会社のロゴデータ(ai)を添付致します。ご提案の際にご利用ください。
■追記■

早速のご提案をありがとうございます。
いくつか、追記事項を記載致します。

1.期間にはまだ余裕がございますが、良いものが出揃った時点でその中から決定、とさせて頂く場合がございます。もし、ご提案をお考えでいらっしゃいましたら、お早めにご提案を頂戴するか、事前にお知らせいただけましたら、その日程までお待ちするよう、申し伝えますのでご相談ください。

2.ご提案頂戴した内容につきまして、フィードバックなどがある場合には頂いた順に、個別にご連絡をさせて頂く場合がございます。フィードバックの内容を元に、再度ご提案いただいても構いません。

3.上記に関連しますが、お一方なんパターン提案を頂戴しても構いません。それぞれ別なご提案として、検討させていただきます。

4.デザイン頂くにあたってのコンセプトや、ポイント、検討した点などが、もしありましたらご説明欄で記載を頂戴できますでしょうか。

5.動きがある部分につきましては、どの部分がどの様に動くのか、言葉では難しいかもしれませんが、簡単にご説明頂戴できましたら助かります。

6.色合いにつきましては、踏襲を基本と思っておりますが、それ以外のご提案がなし、というわけではありません。奇抜なアイディアも歓迎でございます。お一方複数のご提案も歓迎致します。

7.レイアウトについては現在の形式にこだわりはありませんので崩していただいても構いません。

引き続き、ご提案のほどお待ちし申し上げております。
どうぞ宜しく御願致します。

インパクトが強く、印象に残りやすいこと、見たことのある素材などで構成されていない独創的なところがポイントとなりました。
ITらしさがあり、女性向きではないのでその点は修正をお願いしておりますが、申し分のない内容でございました。

当選以外のご提案に付きましても、本件にお時間を頂戴いたしましたこと、心からお礼申し上げます。

本件、皆様からのご応募誠にありがとうございました。
どのご提案も、甲乙つけがたくございまして、別なご縁で機会を頂戴できればと存じます。

皆様ありがとうございました。
またどうぞ、宜しくお願い申し上げます。

```html
<!DOCTYPE html>
<html lang="ja">
<head>
<meta charset="utf-8">
<title>hinata reku</title>
<link href="https://fonts.googleapis.com/css2?family=Noto+Sans+JP:wght@400;500&family=Open+Sans:wght@300;400;600&display=swap" rel="stylesheet">
<style>
:root{
  --red:#c0392b;
  --red-line:#b3261e;
  --black:#0b0b0c;
  --dark:#141416;
  --white:#ffffff;
  --ink:#222222;
  --grey:#8a8a8a;
  --line:#cfcfcf;
}
*{margin:0;padding:0;box-sizing:border-box}
html,body{width:731px;height:1200px;overflow:hidden;background:var(--white)}
body{position:relative;font-family:"Noto Sans JP",sans-serif;color:var(--ink)}
.abs{position:absolute}
.en{font-family:"Open Sans",sans-serif}

/* header */
.site-header{position:absolute;left:0;top:0;width:731px;height:49px;background:var(--black);z-index:3}
.nav-item{position:absolute;top:25px;color:var(--white);font-family:"Open Sans",sans-serif;font-size:9px;line-height:1.1;letter-spacing:.04em}
.nav-item small{display:block;font-family:"Noto Sans JP",sans-serif;font-size:6px;color:#ccc}
.nav-contact{position:absolute;left:230px;top:22px;width:267px;height:26px;background:var(--red);color:var(--white);font-family:"Open Sans",sans-serif;font-size:9px;padding:4px 0 0 10px;line-height:1.1}
.nav-contact small{display:block;font-family:"Noto Sans JP",sans-serif;font-size:6px}
.nav-contact svg{position:absolute;left:83px;top:8px}

/* hero */
.hero{position:absolute;left:0;top:0;width:731px;height:407px;
  background:radial-gradient(ellipse at 55% 35%,#2a7fb8 0%,#164a73 30%,#0b2238 60%,#05090f 100%)}
.hero-title{position:absolute;left:26px;top:196px;color:var(--white);font-family:"Open Sans",sans-serif;font-weight:300;font-size:42px;letter-spacing:.02em}
.hero-brand{position:absolute;left:28px;top:287px;color:var(--white);font-family:"Open Sans",sans-serif;font-size:26px;font-weight:400}

/* vision */
.vision{position:absolute;left:0;top:407px;width:731px;height:223px;background:var(--black)}
.label{position:absolute;font-family:"Open Sans",sans-serif;font-size:10px;letter-spacing:.04em}
.vision-text{position:absolute;left:114px;top:28px;width:400px;color:var(--white);font-size:9.4px;line-height:23px;letter-spacing:.02em}
.more{position:absolute;height:22px;font-family:"Open Sans",sans-serif;font-size:8px;padding:5px 0 0 0;text-align:center}
.more svg{position:absolute;right:10px;top:7px}

/* services */
.services{position:absolute;left:0;top:630px;width:477px;height:220px;background:var(--red)}
.services-photo{position:absolute;left:477px;top:630px;width:254px;height:220px;
  background:linear-gradient(160deg,#5a4b48 0%,#3a302f 50%,#2a2322 100%)}
.svc{position:absolute;color:var(--white);font-size:9.5px;white-space:nowrap}
.svc svg{margin-left:6px;vertical-align:middle}

/* corporate */
.corporate{position:absolute;left:0;top:850px;width:731px;height:268px;background:var(--white)}
.corp-brand{position:absolute;left:44px;top:53px;font-family:"Open Sans",sans-serif;font-size:24px;color:var(--ink)}
.corp-info{position:absolute;left:44px;top:106px;font-size:8.6px;line-height:17.5px}
.map{position:absolute;left:230px;top:40px;width:501px;height:190px;
  background:linear-gradient(135deg,#e9e6df 0%,#dfe3e6 50%,#e6e4dc 100%)}

/* footer */
.site-footer{position:absolute;left:0;top:1118px;width:731px;height:82px;border-top:1px solid var(--ink);background:var(--white)}
.foot-nav{position:absolute;top:12px;font-family:"Open Sans",sans-serif;font-size:8px;text-align:center;line-height:1.1}
.foot-nav small{display:block;font-family:"Noto Sans JP",sans-serif;font-size:5.5px;color:var(--grey)}
.copyright{position:absolute;left:0;top:72px;width:731px;text-align:center;font-family:"Open Sans",sans-serif;font-size:5.5px;color:var(--grey)}
</style>
</head>
<body>

<section class="hero" role="img" aria-label="Photo of glowing blue optical fibers on a dark background"></section>
<h1 class="hero-title">CHANGE THE WORLD</h1>
<div class="hero-brand">hinata reku</div>

<header class="site-header">
  <div class="nav-item" style="left:29px">VISION<small>企業理念</small></div>
  <div class="nav-item" style="left:94px">SERVICES<small>事業内容</small></div>
  <div class="nav-item" style="left:155px">CORPORATE<small>会社概要</small></div>
  <div class="nav-contact">CONTACT<small>お問い合わせ</small>
    <svg width="6" height="9" viewBox="0 0 6 9"><path d="M1 1l3.5 3.5L1 8" stroke="#fff" fill="none" stroke-width="1.3"/></svg>
  </div>
</header>

<section class="vision">
  <div class="label" style="left:57px;top:6px;color:var(--white)">VISION</div>
  <p class="vision-text">どんなビジネスも、お客さまのニーズに支えられ、商品やサービスを届けることでヒト・モノ・カネが循環し、世の中を潤してゆきます。<br>当社も今はまだ小さく、周りの方々の手をお借りして事業を営んでおりますが、いつかはお世話になった以上の価値を、この世の中に還元してゆける大きな企業となってまいります。<br>我々の提供する商品やサービスが、次の世代に多くの道と機会を与え、この世界に貢献できるよう、日々精進してまいります。</p>
  <div class="more" style="left:391px;top:184px;width:112px;border:1px solid var(--red);color:var(--white)">MORE
    <svg width="5" height="8" viewBox="0 0 5 8"><path d="M1 1l3 3-3 3" stroke="#fff" fill="none"/></svg>
  </div>
</section>

<section class="services">
  <div class="label" style="left:50px;top:5px;color:var(--white)">SERVICES</div>
  <div class="svc" style="left:98px;top:57px">システム開発事業<svg width="5" height="8" viewBox="0 0 5 8"><path d="M1 1l3 3-3 3" stroke="#fff" fill="none"/></svg></div>
  <div class="svc" style="left:82px;top:79px">コンサルティング事業<svg width="5" height="8" viewBox="0 0 5 8"><path d="M1 1l3 3-3 3" stroke="#fff" fill="none"/></svg></div>
  <div class="svc" style="left:215px;top:57px">ホテル事業<svg width="5" height="8" viewBox="0 0 5 8"><path d="M1 1l3 3-3 3" stroke="#fff" fill="none"/></svg></div>
  <div class="svc" style="left:225px;top:79px">保育事業<svg width="5" height="8" viewBox="0 0 5 8"><path d="M1 1l3 3-3 3" stroke="#fff" fill="none"/></svg></div>
  <div class="svc en" style="left:65px;top:150px">AI / IoT / ビッグデータ事業<svg width="5" height="8" viewBox="0 0 5 8"><path d="M1 1l3 3-3 3" stroke="#fff" fill="none"/></svg></div>
</section>
<div class="services-photo" role="img" aria-label="Monochrome aerial photo of a dense city crowd"></div>

<section class="corporate">
  <div class="label" style="left:44px;top:8px;color:var(--ink)">CORPORATE</div>
  <div class="corp-brand">hinata reku</div>
  <div class="corp-info">有限会社 hinata reku<br>〒150-0021 東京都渋谷区恵比寿西 3-8-12<br>ひなたレクビル 4F<br>TEL. 03-5555-0142</div>
  <div class="more" style="left:44px;top:194px;width:111px;border:1px solid var(--red);color:var(--ink)">MORE
    <svg width="5" height="8" viewBox="0 0 5 8"><path d="M1 1l3 3-3 3" stroke="#c0392b" fill="none"/></svg>
  </div>
  <div class="map" role="img" aria-label="Street map showing the office location"></div>
</section>

<!-- decorative red grid lines -->
<svg class="abs" style="left:0;top:0;z-index:2" width="731" height="1118" viewBox="0 0 731 1118" aria-hidden="true">
  <g stroke="var(--red-line)" stroke-width="1" fill="none" opacity=".85">
    <line x1="0" y1="174" x2="731" y2="174"/>
    <line x1="0" y1="262" x2="731" y2="262"/>
    <line x1="155" y1="75" x2="155" y2="407"/>
    <line x1="347" y1="90" x2="347" y2="300"/>
    <line x1="24" y1="407" x2="24" y2="630"/>
    <line x1="0" y1="565" x2="280" y2="565"/>
  </g>
  <g stroke="#ffffff" stroke-width=".8" fill="none" opacity=".7">
    <line x1="0" y1="697" x2="445" y2="697"/>
    <line x1="40" y1="795" x2="445" y2="795"/>
    <line x1="190" y1="630" x2="190" y2="885"/>
    <line x1="280" y1="630" x2="280" y2="850"/>
  </g>
</svg>

<footer class="site-footer">
  <div class="foot-nav" style="left:220px">TOP<small>トップ</small></div>
  <div class="foot-nav" style="left:268px">VISION<small>企業理念</small></div>
  <div class="foot-nav" style="left:326px">SERVICES<small>事業内容</small></div>
  <div class="foot-nav" style="left:393px">CORPORATE<small>会社概要</small></div>
  <div class="foot-nav" style="left:471px">CONTACT<small>お問い合わせ</small></div>
  <p class="copyright">Copyright©2019 hinata reku Co.,Ltd. All Rights Reserved</p>
</footer>

</body>
</html>
```